COMMERCIAL DOOR REPAIR
BUSINESS CARDS, LETTERHEAD, ENVELOPES, FAX COVER, EMAIL SIGNATURE
Rob Whitfield
NFPEI Certified Door Inspector
1752 E Pinnell Ln Glendale, AZ 85317
service@robsgatefix.com
www.robsgatefix.com
ROC# 514037
Not sure if font in logo can be used - open to other fonts as well. just no script or femine fonts. Not sure if all items on back will fit - open to re-wording, suggestions, etc.
24 Hour Emergency Services Available Specializing in: Automatic Doors Manual Doors Vitrelon Glass Doors Hollow Metal Doors Revolving Doors Also specializing in: Glass Mirrors Locksmithing Shower Doors Roof Hatches Re-seals Board-Ups

```html
<!DOCTYPE html>
<html lang="en">
<head>
<meta charset="utf-8">
<title>Harbor Door Works — Stationery Set</title>
<link href="https://fonts.googleapis.com/css2?family=Open+Sans:wght@400;600;700&display=swap" rel="stylesheet">
<style>
:root{
  --bg:#ece9e4;
  --paper:#ffffff;
  --paper-shade:#eef1f5;
  --blue:#1f78c8;
  --blue-dark:#0f5aa6;
  --blue-light:#4aa3e6;
  --red:#d62a2a;
  --ink:#3a3f47;
  --muted:#9aa3ad;
}
*{box-sizing:border-box;margin:0;padding:0}
html,body{width:1200px;height:809px;overflow:hidden}
body{background:var(--bg);font-family:"Open Sans",Arial,sans-serif;color:var(--ink);position:relative}
.piece{position:absolute;background:var(--paper);box-shadow:0 2px 6px rgba(0,0,0,.18);overflow:hidden}
.piece.blue{background:linear-gradient(160deg,var(--blue-light),var(--blue-dark))}
.wave{position:absolute;left:0;bottom:0;width:100%;height:18%;display:block}
.brand{position:absolute;display:flex;align-items:center;gap:3px;font-weight:700;color:var(--blue-dark);white-space:nowrap;text-transform:uppercase}
.brand .mark{background:var(--blue);width:1.3em;height:1.3em;display:inline-block;flex:none}
.brand.white{color:#fff}.brand.white .mark{background:#fff}
.tiny{position:absolute;font-size:4px;line-height:1.5;color:var(--muted)}
.doc-title{position:absolute;font-size:6px;font-weight:700;color:var(--ink)}
.table{position:absolute;border:0.5px solid var(--muted)}
.table .head{height:6px;background:var(--blue)}
.badge{position:absolute;border-radius:50%;background:var(--red);color:#fff;font-weight:700;display:flex;align-items:center;justify-content:center}
.cd{position:absolute;border-radius:50%;background:radial-gradient(circle,#fff 0 14%,var(--paper-shade) 15% 100%);box-shadow:0 2px 6px rgba(0,0,0,.2);overflow:hidden}
.cover-title{position:absolute;font-weight:700;color:var(--blue)}
.cover-sub{position:absolute;font-weight:600;color:var(--blue-dark)}
.thanks{position:absolute;color:#fff;font-weight:600;text-align:center;line-height:1.25}
.flap{position:absolute;background:var(--blue)}
</style>
</head>
<body>

<!-- letterhead -->
<div class="piece" style="left:34px;top:24px;width:163px;height:233px">
  <div class="brand" style="left:12px;top:14px;font-size:6px"><span class="mark"></span>Harbor Door Works</div>
  <p class="tiny" style="left:12px;top:40px;width:138px">Dear Client, thank you for choosing our team for your commercial door needs. We look forward to serving you again soon with fast repair work.</p>
  <svg class="wave" viewBox="0 0 100 20" preserveAspectRatio="none"><path d="M0 9Q50-1 100 11V20H0Z" fill="var(--blue)"/><path d="M0 7Q50-3 100 9" stroke="var(--red)" stroke-width="1.2" fill="none"/></svg>
</div>

<!-- invoice -->
<div class="piece" style="left:230px;top:24px;width:164px;height:233px">
  <div class="brand" style="left:12px;top:14px;font-size:6px"><span class="mark"></span>Harbor Door Works</div>
  <div class="doc-title" style="right:12px;top:14px">INVOICE</div>
  <div class="table" style="left:12px;top:52px;width:140px;height:100px"><div class="head"></div></div>
  <svg class="wave" viewBox="0 0 100 20" preserveAspectRatio="none"><path d="M0 9Q50-1 100 11V20H0Z" fill="var(--blue)"/><path d="M0 7Q50-3 100 9" stroke="var(--red)" stroke-width="1.2" fill="none"/></svg>
</div>

<!-- quote -->
<div class="piece" style="left:427px;top:24px;width:163px;height:233px">
  <div class="brand" style="left:12px;top:14px;font-size:6px"><span class="mark"></span>Harbor Door Works</div>
  <div class="doc-title" style="right:12px;top:14px">QUOTE</div>
  <div class="table" style="left:12px;top:52px;width:140px;height:100px"><div class="head"></div></div>
  <svg class="wave" viewBox="0 0 100 20" preserveAspectRatio="none"><path d="M0 9Q50-1 100 11V20H0Z" fill="var(--blue)"/><path d="M0 7Q50-3 100 9" stroke="var(--red)" stroke-width="1.2" fill="none"/></svg>
</div>

<!-- fax cover -->
<div class="piece" style="left:619px;top:24px;width:163px;height:233px">
  <div class="brand" style="left:12px;top:14px;font-size:6px"><span class="mark"></span>Harbor Door Works</div>
  <div class="doc-title" style="left:12px;top:30px">FAX</div>
  <div class="table" style="left:12px;top:62px;width:140px;height:40px"><div class="head" style="width:30px"></div></div>
  <p class="tiny" style="left:12px;top:110px;width:138px">To, From, Date, Pages, Re: please review the attached quote and call us back.</p>
  <svg class="wave" viewBox="0 0 100 20" preserveAspectRatio="none"><path d="M0 9Q50-1 100 11V20H0Z" fill="var(--blue)"/><path d="M0 7Q50-3 100 9" stroke="var(--red)" stroke-width="1.2" fill="none"/></svg>
</div>

<!-- closed folder -->
<div class="piece" style="left:830px;top:24px;width:339px;height:331px;background:linear-gradient(180deg,#fff 60%,var(--paper-shade))">
  <div style="position:absolute;left:0;top:0;width:168px;height:100%;border-right:1px solid #dde2e8"></div>
  <div class="brand" style="left:20px;top:230px;font-size:8px"><span class="mark"></span>Harbor Door Works</div>
  <div class="tiny" style="right:18px;top:276px;color:var(--blue-dark);font-size:5px">www.harbordoorworks.com</div>
  <svg class="wave" viewBox="0 0 100 20" preserveAspectRatio="none"><path d="M0 9Q50-1 100 11V20H0Z" fill="var(--blue)"/><path d="M0 7Q50-3 100 9" stroke="var(--red)" stroke-width="1.2" fill="none"/></svg>
</div>

<!-- DL envelope front -->
<div class="piece" style="left:34px;top:264px;width:278px;height:120px">
  <div class="brand" style="left:14px;top:12px;font-size:6px"><span class="mark"></span>Harbor Door Works</div>
  <p class="tiny" style="left:14px;top:28px">408 N Corvell Ave<br>Peoria, AZ 85345</p>
  <svg class="wave" viewBox="0 0 100 20" preserveAspectRatio="none"><path d="M0 9Q50-1 100 11V20H0Z" fill="var(--blue)"/><path d="M0 7Q50-3 100 9" stroke="var(--red)" stroke-width="1.2" fill="none"/></svg>
</div>

<!-- DL envelope back -->
<div class="piece" style="left:324px;top:264px;width:295px;height:120px">
  <svg style="position:absolute;inset:0;width:100%;height:100%" viewBox="0 0 100 40" preserveAspectRatio="none"><path d="M0 0H100V8L50 22L0 8Z" fill="var(--blue)"/><path d="M0 8L50 22L100 8" stroke="var(--red)" stroke-width=".5" fill="none"/></svg>
  <div class="brand white" style="left:112px;top:20px;font-size:6px"><span class="mark"></span>Harbor Door Works</div>
</div>

<!-- compliment slip -->
<div class="piece" style="left:631px;top:307px;width:89px;height:46px">
  <div class="brand" style="left:6px;top:6px;font-size:4px"><span class="mark"></span>Harbor Door Works</div>
  <p class="tiny" style="left:6px;top:18px;font-size:3px">With compliments</p>
</div>

<!-- open folder -->
<div class="piece blue" style="left:799px;top:367px;width:370px;height:202px">
  <div class="badge" style="left:22px;top:14px;width:44px;height:44px;font-size:16px">24</div>
  <div class="brand white" style="left:24px;top:120px;font-size:7px"><span class="mark"></span>Harbor Door Works</div>
  <div class="piece" style="left:196px;top:12px;width:150px;height:180px;box-shadow:0 1px 4px rgba(0,0,0,.3)">
    <div class="brand" style="left:10px;top:10px;font-size:5px"><span class="mark"></span>Harbor Door Works</div>
    <p class="tiny" style="left:10px;top:34px;width:128px">Specializing in automatic, manual, Vitrelon glass, hollow metal and revolving doors.</p>
    <div class="piece" style="left:40px;top:136px;width:60px;height:32px;background:#fff"></div>
  </div>
</div>

<!-- business card front -->
<div class="piece" style="left:34px;top:408px;width:139px;height:65px">
  <div class="brand" style="left:8px;top:6px;font-size:5px"><span class="mark"></span>Harbor Door Works</div>
  <p class="tiny" style="left:8px;top:18px;font-size:3.5px;line-height:1.4;color:var(--ink)">Lena Marsh<br>Certified Door Inspector<br>(602) 555-0148<br>office@harbordoorworks.com<br>ROC# 772916</p>
  <svg class="wave" viewBox="0 0 100 20" preserveAspectRatio="none"><path d="M0 9Q50-1 100 11V20H0Z" fill="var(--blue)"/><path d="M0 7Q50-3 100 9" stroke="var(--red)" stroke-width="1.2" fill="none"/></svg>
</div>

<!-- business card second -->
<div class="piece" style="left:180px;top:408px;width:132px;height:65px">
  <div class="brand" style="left:8px;top:6px;font-size:5px"><span class="mark"></span>Harbor Door Works</div>
  <p class="tiny" style="left:8px;top:18px;font-size:3.5px;line-height:1.4;color:var(--ink)">Automatic Doors<br>Manual Doors<br>Vitrelon Glass Doors<br>Hollow Metal Doors<br>Revolving Doors</p>
  <svg class="wave" viewBox="0 0 100 20" preserveAspectRatio="none"><path d="M0 9Q50-1 100 11V20H0Z" fill="var(--blue)"/><path d="M0 7Q50-3 100 9" stroke="var(--red)" stroke-width="1.2" fill="none"/></svg>
</div>

<!-- business card back -->
<div class="piece blue" style="left:115px;top:492px;width:111px;height:55px">
  <div class="badge" style="left:36px;top:6px;width:26px;height:18px;font-size:9px">24</div>
  <p class="tiny" style="left:8px;top:30px;width:95px;color:#fff;font-size:3.5px;text-align:center">24 Hour Emergency Services Available</p>
</div>

<!-- card envelope -->
<div class="piece" style="left:341px;top:413px;width:259px;height:139px;background:linear-gradient(180deg,#fff,var(--paper-shade))">
  <div class="brand" style="left:86px;top:52px;font-size:6px"><span class="mark"></span>Harbor Door Works</div>
  <svg class="wave" viewBox="0 0 100 20" preserveAspectRatio="none"><path d="M0 9Q50-1 100 11V20H0Z" fill="var(--blue)"/><path d="M0 7Q50-3 100 9" stroke="var(--red)" stroke-width="1.2" fill="none"/></svg>
</div>

<!-- CD -->
<div class="cd" style="left:619px;top:439px;width:106px;height:106px">
  <div class="brand" style="left:20px;top:20px;font-size:5px"><span class="mark"></span>Harbor Door Works</div>
  <svg class="wave" viewBox="0 0 100 20" preserveAspectRatio="none" style="height:26%"><path d="M0 9Q50-1 100 11V20H0Z" fill="var(--blue)"/><path d="M0 7Q50-3 100 9" stroke="var(--red)" stroke-width="1.2" fill="none"/></svg>
</div>

<!-- presentation cover -->
<div class="piece" style="left:34px;top:605px;width:235px;height:187px">
  <div class="brand" style="left:12px;top:10px;font-size:6px"><span class="mark"></span>Harbor Door Works</div>
  <div class="cover-title" style="left:0;width:100%;text-align:center;top:72px;font-size:13px">Your Titles Here</div>
  <div class="cover-sub" style="left:0;width:100%;text-align:center;top:92px;font-size:8px">Subtitle Here</div>
  <svg class="wave" viewBox="0 0 100 20" preserveAspectRatio="none"><path d="M0 9Q50-1 100 11V20H0Z" fill="var(--blue)"/><path d="M0 7Q50-3 100 9" stroke="var(--red)" stroke-width="1.2" fill="none"/></svg>
</div>

<!-- report cover -->
<div class="piece" style="left:293px;top:605px;width:235px;height:187px">
  <div class="brand" style="left:12px;top:12px;font-size:6px"><span class="mark"></span>Harbor Door Works</div>
  <div class="cover-title" style="left:12px;top:34px;font-size:9px">Your Titles Here</div>
  <div class="cover-sub" style="left:12px;top:48px;font-size:6px">Subtitle Here</div>
  <svg class="wave" viewBox="0 0 100 20" preserveAspectRatio="none"><path d="M0 9Q50-1 100 11V20H0Z" fill="var(--blue)"/><path d="M0 7Q50-3 100 9" stroke="var(--red)" stroke-width="1.2" fill="none"/></svg>
</div>

<!-- closing slide -->
<div class="piece blue" style="left:547px;top:605px;width:233px;height:187px">
  <div class="thanks" style="left:10px;right:10px;top:72px;font-size:12px">Thank you very much<br>for your valuable time.</div>
</div>

<!-- large envelope -->
<div class="piece" style="left:804px;top:607px;width:365px;height:185px">
  <div class="flap" style="right:0;top:0;width:34px;height:100%"></div>
  <div class="brand" style="left:14px;top:10px;font-size:6px"><span class="mark"></span>Harbor Door Works</div>
  <p class="tiny" style="left:14px;top:24px">408 N Corvell Ave, Peoria, AZ 85345</p>
  <svg class="wave" viewBox="0 0 100 20" preserveAspectRatio="none" style="width:91%"><path d="M0 9Q50-1 100 11V20H0Z" fill="var(--blue)"/><path d="M0 7Q50-3 100 9" stroke="var(--red)" stroke-width="1.2" fill="none"/></svg>
</div>

</body>
</html>
```